Asia based real estate financing firm needs and AWESOME design for a biz card -Harbor Lending Circle

Looking for a stylish, & corporate-looking business card for a real estate financing brokerage firm in Asia, offering global mortgage loans. I uploaded our current logos. We would like to add a splash of color (perhaps the house icon) or any other suggestions are open. For the winning designer, we have a lot of work! Thanks and best of luck!

Target Market(s)

Real estate investors globally. We want to look more like a BANK and NOT a real estate company. Please don't play up on a "house" design.

Industry/Entity Type

Banking

Contact Information for Business Card

Harbor Lending Circle
Peter Wilks
Co-Founder | Partner

14 Cassia Lane, Suite 310
Singapore 047219
www.hlc-example.asia
peterwilks@hlc-example.asia
+65 555-0142
WeChat: peterwilks

Colors

Designer to choose colors to be used in the design.

Requirements
Must have
• Must have the standard business requirements for a card; name, address, email, etc
• Can be horizontal or vertical.
Nice to have
• It would be great to see some sort of variation to the logo with a pop of color. Red is good as we're in Asia, however, other options work as well.
• Our tag line is - Borderless mortgages. It doesn't have to be on the card but might be nice.
• I'd like to start seeing our tagline within the cards as well. - Borderless mortgages.
• Also, please add our location. The location for this card is Singapore so perhaps it can be highlighted or emphasised in some way.
• Singapore | Hong Kong | Shanghai | Manila
• As we will soon open an office in Shanghai, having an option for both languages would be great.
Should not have
• I'm exceited and open to your creativity ... knock it out of the park!

```html
<!DOCTYPE html>
<html lang="en">
<head>
<meta charset="utf-8">
<title>Harbor Lending Circle – Business Card</title>
<link href="https://fonts.googleapis.com/css2?family=Cinzel:wght@500&family=Saira+Semi+Condensed:wght@400;500&display=swap" rel="stylesheet">
<style>
  :root {
    --backdrop: #2a2a2a;
    --brand-blue: #2a5cb3;
    --brand-red: #c8202b;
    --card-white: #ffffff;
    --ink-blue: #2456a8;
  }
  * { margin: 0; padding: 0; box-sizing: border-box; }
  html, body { width: 1200px; height: 900px; overflow: hidden; }
  body {
    background: var(--backdrop);
    position: relative;
    font-family: "Saira Semi Condensed", sans-serif;
  }
  .card {
    position: absolute;
    left: 250px;
    width: 700px;
    height: 400px;
    overflow: hidden;
    box-shadow: 0 10px 30px rgba(0,0,0,.45);
  }
  .card-front {
    top: 35px;
    background: linear-gradient(90deg, var(--brand-blue) 0%, #7a4e80 45%, var(--brand-red) 100%);
  }
  .card-front .edge-strip {
    position: absolute; left: 0; right: 0; bottom: 0; height: 14px;
    background: var(--card-white);
  }
  .wordmark {
    position: absolute; left: 0; right: 0;
    text-align: center;
    font-family: "Cinzel", serif;
    font-weight: 500;
    letter-spacing: 2px;
    white-space: nowrap;
  }
  .card-front .wordmark { top: 140px; font-size: 40px; color: var(--card-white); }
  .card-front .site {
    position: absolute; left: 0; right: 0; top: 262px;
    text-align: center;
    color: var(--card-white);
    font-size: 18px;
    letter-spacing: 6px;
    white-space: nowrap;
  }
  .card-back { top: 465px; background: var(--card-white); }
  .card-back .wordmark { top: 78px; font-size: 40px; color: var(--brand-red); }
  .identity {
    position: absolute; right: 365px; top: 178px;
    text-align: right; white-space: nowrap;
  }
  .identity .name {
    font-size: 40px; font-weight: 400; color: var(--brand-red);
    line-height: 1; text-transform: uppercase;
  }
  .identity .role { font-size: 19px; color: var(--ink-blue); margin-top: 8px; }
  .divider {
    position: absolute; left: 365px; top: 180px; width: 2px; height: 100px;
    background: var(--ink-blue);
  }
  .contacts {
    position: absolute; left: 385px; top: 180px;
    list-style: none; color: var(--ink-blue); font-size: 17px; font-weight: 500;
    white-space: nowrap;
  }
  .contacts li { display: flex; align-items: center; height: 25px; }
  .contacts svg { width: 15px; height: 15px; margin-right: 9px; fill: var(--brand-red); flex: none; }
  .footer-band { position: absolute; left: 0; bottom: 0; width: 700px; height: 80px; }
  .address {
    position: absolute; left: 70px; width: 520px; bottom: 26px;
    text-align: center; color: var(--card-white); font-size: 17px; font-weight: 500;
    white-space: nowrap;
  }
</style>
</head>
<body>
  <section class="card card-front">
    <div class="wordmark">HARBOR LENDING CIRCLE</div>
    <div class="site">www.hlc-example.asia</div>
    <div class="edge-strip"></div>
  </section>

  <section class="card card-back">
    <div class="wordmark">HARBOR LENDING CIRCLE</div>

    <div class="identity">
      <h1 class="name">Peter Wilks</h1>
      <p class="role">Co-Founder | Partner</p>
    </div>

    <div class="divider"></div>

    <ul class="contacts">
      <li><svg viewBox="0 0 16 16"><circle cx="8" cy="8" r="7"/><path d="M1 8h14M8 1c-3 3-3 11 0 14M8 1c3 3 3 11 0 14" stroke="#fff" stroke-width="1.2" fill="none"/></svg>www.hlc-example.asia</li>
      <li><svg viewBox="0 0 16 16"><rect x="1" y="3" width="14" height="10" rx="1"/><path d="M1 4l7 5 7-5" stroke="#fff" stroke-width="1.2" fill="none"/></svg>peterwilks@hlc-example.asia</li>
      <li><svg viewBox="0 0 16 16"><path d="M3 1l3 3-1.5 2c1 2 3 4 5 5L11.5 9.5l3 3-2 2.5C7 14 2 9 1 3z"/></svg>+65 555-0142</li>
      <li>WeChat: peterwilks</li>
    </ul>

    <svg class="footer-band" viewBox="0 0 700 80" aria-hidden="true">
      <rect x="0" y="30" width="700" height="20" fill="var(--brand-blue)"/>
      <polygon points="50,10 610,10 640,80 20,80" fill="var(--brand-red)"/>
    </svg>
    <p class="address">14 Cassia Lane, Suite 310, Singapore 047219</p>
  </section>
</body>
</html>
```